Leading Nutrition Company Needs a Stylish Label Design!

We need a label/packaging design for our new cutting-edge detox called "Clear Tide". It is an all organic detox that removes toxins, harsh-chemicals, herbicides, pesticides and heavy metals from the body. It essentially turns everything you eat into organic whole foods and without all the chemicals in our bodies, we run at optimal performance.

We are attempting to blend a modern, simplistic design for our label.
We would like to see designs that use flat grays, silvers and blacks. We would also like to see pops of green and or blue in the design. Overall design will be a modern, contemporary matte finish with pops of color in either a pattern design or colored lettering. The final design should convey a high-end, exclusive health product.

Target Market(s)

Health conscious individuals and those seeking to pass an upcoming drug test. Athletes, nutritionist, dietitians ranging from 18-70 years of age.

Industry/Entity Type

Health

Font styles to use
Other font styles liked:
• Unique modern fonts

Colors
b1b1b1
9d9d9d
474747
33a6d7
0192cd
9ccb3b

Requirements
Must have
• Must be modern and simplistic

Pops of color - Don't need to be matte

Matte finishes for background
-Light grays, graphite, light silvers etc

Lettering must be modern and unique

Label type wil be a "shrink label" for an 8 oz boston squat bottle
-See attached link for bottle

"Clear Tide" some where on label

Company logo some where on label
-See attached files for logo
Nice to have
• Cool background designs that provide depth to the design.

A strip of pattern design running vertically or horizontally to capture the eye.
-See attached pictures for examples
Should not have
• Script or Normal fonts

```html
<!DOCTYPE html>
<html lang="en">
<head>
<meta charset="utf-8">
<title>Clear Tide – Detox Label</title>
<link rel="stylesheet" href="https://fonts.googleapis.com/css2?family=Dosis:wght@400;500;600&family=Ubuntu+Condensed&display=swap">
<style>
  :root {
    --page: #ffffff;
    --panel: #a9aaac;
    --panel-light: #b4b5b7;
    --panel-dark: #9d9e a0;
    --graphite: #474747;
    --ring: #3b3b3d;
    --lime: #b3d335;
    --white: #ffffff;
    --stamp: #d2d3d5;
    --fruit-a: #e8a23a;
    --fruit-b: #c9b04a;
    --fruit-c: #b4453f;
  }
  html, body {
    margin: 0;
    padding: 0;
    width: 1200px;
    height: 1124px;
    overflow: hidden;
    background: var(--page);
  }
  .label-sheet {
    display: block;
    width: 1200px;
    height: 1124px;
  }
  .panel-bg { fill: url(#panelShade); }
  .ring-dark { fill: none; stroke: var(--ring); stroke-width: 16; }
  .ring-lime { fill: none; stroke: var(--lime); stroke-width: 30; }
  .brand-block { fill: var(--lime); }
  .notch { fill: var(--panel); }
  .tagline {
    font-family: "Dosis", sans-serif;
    font-weight: 500;
    fill: var(--white);
  }
  .product-name {
    font-family: "Dosis", sans-serif;
    font-weight: 500;
  }
  .product-name--dark { fill: var(--graphite); }
  .product-name--light { fill: var(--white); }
  .flavour {
    font-family: "Dosis", sans-serif;
    font-weight: 500;
    font-size: 36px;
    fill: var(--graphite);
  }
  .volume {
    font-family: "Dosis", sans-serif;
    font-weight: 500;
    font-size: 28px;
    fill: var(--graphite);
  }
  .fruit-visual { fill: url(#fruitTones); }
  .description {
    margin: 0;
    font-family: "Ubuntu Condensed", sans-serif;
    font-size: 11.6px;
    line-height: 1.3;
    color: var(--white);
    text-align: justify;
    text-align-last: center;
  }
  .maker-mark { fill: none; stroke: var(--white); stroke-width: 6; }
  .maker-name {
    font-family: "Dosis", sans-serif;
    font-weight: 600;
    font-size: 24px;
    fill: var(--white);
  }
  .fine-print {
    margin: 0;
    font-family: "Ubuntu Condensed", sans-serif;
    font-size: 10.4px;
    line-height: 1.3;
    color: var(--graphite);
    text-align: center;
  }
  .batch-label {
    font-family: "Ubuntu Condensed", sans-serif;
    font-size: 9.5px;
    fill: var(--graphite);
  }
  .batch-box { fill: var(--stamp); }
</style>
</head>
<body>
<svg class="label-sheet" viewBox="0 0 960 899.2" xmlns="http://www.w3.org/2000/svg">
  <defs>
    <linearGradient id="panelShade" x1="0" y1="0" x2="1" y2="1">
      <stop offset="0" stop-color="#b3b4b6"/>
      <stop offset="0.5" stop-color="#a8a9ab"/>
      <stop offset="1" stop-color="#a2a3a5"/>
    </linearGradient>
    <radialGradient id="fruitTones" cx="0.5" cy="0.55" r="0.6">
      <stop offset="0" stop-color="#e8a23a"/>
      <stop offset="0.55" stop-color="#c9b04a"/>
      <stop offset="1" stop-color="#b4453f" stop-opacity="0.7"/>
    </radialGradient>
    <clipPath id="frontClip"><rect x="15" y="15" width="425" height="865"/></clipPath>
    <clipPath id="backClip"><rect x="522" y="15" width="425" height="865"/></clipPath>
  </defs>

  <!-- Front panel -->
  <g class="front-panel">
    <rect class="panel-bg" x="15" y="15" width="425" height="865"/>
    <g clip-path="url(#frontClip)">
      <circle class="ring-dark" cx="445" cy="22" r="82"/>
      <circle class="ring-lime" cx="15" cy="880" r="222"/>
    </g>

    <rect class="brand-block" x="93" y="133" width="282" height="305"/>
    <rect class="notch" x="188" y="125" width="97" height="22"/>
    <rect class="notch" x="130" y="425" width="215" height="15"/>

    <text class="tagline" x="234" y="150" font-size="30" text-anchor="middle">detox</text>
    <text class="product-name product-name--dark" x="110" y="275" font-size="150" textLength="250" lengthAdjust="spacingAndGlyphs">CLEAR</text>
    <text class="product-name product-name--light" x="110" y="413" font-size="150" textLength="245" lengthAdjust="spacingAndGlyphs">TIDE</text>
    <text class="tagline" x="240" y="465" font-size="28" text-anchor="middle">dietary supplement</text>

    <text class="flavour" x="240" y="547" text-anchor="middle">aloe vera, apple</text>
    <text class="flavour" x="243" y="587" text-anchor="middle">&amp; blueberry juice</text>

    <text class="volume" x="240" y="832" text-anchor="middle">8 oz (237ml)</text>
  </g>

  <!-- Back panel -->
  <g class="back-panel">
    <rect class="panel-bg" x="522" y="15" width="425" height="865"/>
    <g clip-path="url(#backClip)">
      <circle class="ring-dark" cx="517" cy="22" r="82"/>
      <circle class="ring-lime" cx="990" cy="780" r="150"/>
    </g>

    <ellipse class="fruit-visual" cx="732" cy="222" rx="152" ry="160" role="img" aria-label="Arrangement of fresh tropical fruits: pineapple, mango, orange, kiwi, pomegranate, bananas and passion fruit"/>

    <foreignObject x="568" y="416" width="337" height="130">
      <p xmlns="http://www.w3.org/1999/xhtml" class="description">Morbi consectetur est magna, vitae mattis nisl suscipit non. Etiam euismod, justo ac facilisis posuere, risus augue dictum dolor, eget dictum neque erat vel nisl. Fusce vitae bibendum lacus. Quisque consequat diam libero, vitae cursus erat suscipit sit amet. Quisque lacus neque, viverra sed commodo a, lacinia at mauris. Aliquam lacus leo, elementum at ornare a, facilisis ut nibh. Mauris enim diam, blandit sit amet consectetur at, consequat vel sem.</p>
    </foreignObject>

    <g class="maker">
      <circle class="maker-mark" cx="640" cy="640" r="62"/>
      <text class="maker-name" x="640" y="648" text-anchor="middle">vita brook</text>
    </g>

    <foreignObject x="540" y="738" width="200" height="45">
      <p xmlns="http://www.w3.org/1999/xhtml" class="fine-print">Lorem ipsum dolor sit amet, consectetur adipiscing elit. In quis urna ultricies, consectetur erat quis, ullamcorper purus.</p>
    </foreignObject>

    <text class="batch-label" x="540" y="802">Lot#:</text>
    <text class="batch-label" x="542" y="813">Exp:</text>
    <rect class="batch-box" x="565" y="792" width="176" height="46"/>
  </g>
</svg>
</body>
</html>
```